Create a new website for "The Arcade at Fernbrook"

I need a website for a shopping center in Larkfield USA. I want a classy high end look with high end motion videos (which I will provide).
The purpose of website is to attract new tenants to fill up vacant office spaces we have.
we will highlight existing cool stores and advertise that this is a cool place to start a new tenants business or office . ideally IT businesses in Alpharetta city in Georgia state in USA

Target Market(s)

commercial office tenants

Industry/Entity Type

Real Estate

Contact Information for Business Card

classy high end design
Arcade at Fernbrook
address:
2870 Briarwell Pkwy
Larkfield GA 30917

Logo Text

I am open. Anything that attracts new IT tech tenants to lease up shopping center/ office space

Coding

Coded - Design and coding required

Number of Pages Required

5+ page

Requirements
Must have
• easy to browse

here is a link to some photos. i will provide videos shortly

http://www.tomsereph.com/2014/04/Building-Photos-3/n-5N2dg/
Nice to have
• please look at some of mall websites i like. Moving videos and images on home page

I really like this one: https://www.plazaatcresthollow.com/

others are

https://lindorecenter.com/

https://www.discoverbrisket.com/

```html
<!DOCTYPE html>
<html lang="en">
<head>
<meta charset="utf-8">
<title>The Arcade at Fernbrook</title>
<link rel="stylesheet" href="https://fonts.googleapis.com/css2?family=Raleway:ital,wght@0,300;0,400;0,500;0,600;1,400&display=swap">
<style>
:root{
  --accent:#6f86c6;
  --accent-dark:#5b70ad;
  --ink:#1f1f1f;
  --muted:#666;
  --soft-bg:#f4f4f4;
  --line:#e2e2e2;
  --contact-bg:#333333;
  --footer-bg:#2b2b2b;
  --footer-text:#cfcfcf;
  --white:#fff;
}
*{box-sizing:border-box;margin:0;padding:0}
html,body{width:1200px;height:3075px;overflow:hidden}
body{font-family:'Raleway',sans-serif;color:var(--ink);background:var(--white);position:relative}

.hero{position:absolute;left:0;top:0;width:1200px;height:523px;background:linear-gradient(180deg,#2b3f86 0%,#4a5fa8 35%,#7a6f6a 62%,#3d3a38 80%,#5a5f66 100%)}
.brand{position:absolute;left:0;top:0;width:432px;height:105px;background:rgba(80,100,190,.85);color:var(--white);display:flex;flex-direction:column;justify-content:center;padding-left:172px}
.brand small{font-size:17px;font-weight:300}
.brand strong{font-size:34px;font-weight:300;line-height:1}
.main-nav{position:absolute;left:432px;top:0;width:768px;height:105px;background:var(--white);display:flex;align-items:center;padding-left:70px;gap:20px;font-size:14.5px;color:#333}
.main-nav a{text-decoration:none;color:inherit;letter-spacing:.2px}
.main-nav .active{position:relative}
.main-nav .active::before{content:"";position:absolute;left:-8px;right:-8px;top:-52px;height:2px;background:#c8cfdf}
.main-nav .search{margin-left:36px}

.intro{position:absolute;left:0;top:473px;width:753px;height:134px;background:var(--white)}
.intro h1{position:absolute;left:172px;top:32px;font-size:24px;font-weight:400;line-height:35px}
.intro h1 em{font-weight:400}
.btn{display:inline-flex;align-items:center;gap:18px;background:var(--accent);color:var(--white);text-decoration:none;font-size:17px}
.intro .btn{position:absolute;left:530px;top:36px;height:44px;padding:0 22px 0 28px}
.intro .note{position:absolute;left:531px;top:88px;font-size:11.5px;color:var(--muted)}
.intro .note i{display:inline-block;width:4px;height:4px;background:var(--accent);margin:0 6px 2px;vertical-align:middle}
.hours{position:absolute;left:753px;top:523px;width:447px;height:84px;background:var(--accent);color:var(--white)}
.hours svg{position:absolute;left:-2px;top:8px}
.hours p{position:absolute;left:80px;top:16px;font-size:21px;font-weight:300}
.hours b{display:block;font-weight:600;font-size:22px;margin-top:2px}

.sec-title{text-align:center;font-weight:400}
.rule{position:relative;height:1px;background:var(--line);width:564px;margin:0 auto}
.rule::after{content:"";position:absolute;left:179px;width:206px;top:-1px;height:2px;background:var(--accent)}

.why{position:absolute;left:0;top:607px;width:1200px;height:494px;background:var(--soft-bg)}
.why .sec-title{position:absolute;top:66px;width:100%;font-size:27px;line-height:28px}
.why .sec-title span{display:block;font-size:20px;line-height:24px}
.why .rule{position:absolute;left:318px;top:138px}
.features{position:absolute;top:180px;left:172px;display:flex;gap:60px}
.feature{width:244px;text-align:center}
.feature svg{display:block;margin:0 auto 18px}
.feature h3{font-size:21px;font-weight:400;margin-bottom:10px}
.feature p{font-size:13px;color:var(--muted);line-height:16px}

.band{position:absolute;left:0;top:1101px;width:1200px;height:501px;background:linear-gradient(180deg,#3a63c4 0%,#5f86d4 45%,#d8d8d4 70%,#7b6a4f 100%)}
.partners{position:absolute;left:184px;top:1196px;width:832px;height:462px;background:var(--white);box-shadow:0 2px 8px rgba(0,0,0,.08)}
.partners .sec-title{margin-top:40px;font-size:24px;line-height:30px}
.partners .sec-title span{display:block;font-size:20px;line-height:26px}
.partners .rule{margin-top:20px}
.tenants{display:grid;grid-template-columns:repeat(4,1fr);width:680px;margin:40px auto 0;row-gap:68px;text-align:center;font-size:27px;font-weight:500;color:#222}
.partners .btn{position:absolute;left:331px;top:372px;height:42px;padding:0 16px 0 20px;font-size:17px}

.gallery-title{position:absolute;top:1700px;width:1200px;font-size:27px}
.gallery-rule{position:absolute;left:318px;top:1755px}
.shot{position:absolute}

.map{position:absolute;left:0;top:2289px;width:600px;height:422px;background:linear-gradient(135deg,#2f2f2f,#242428 60%,#2e2a33)}
.contact{position:absolute;left:600px;top:2289px;width:600px;height:422px;background:var(--contact-bg);color:var(--white)}
.contact h2{position:absolute;left:111px;top:58px;font-size:24px;font-weight:500}
.contact .line{position:absolute;left:111px;top:118px;width:350px;height:1px;background:#555}
.contact .line::after{content:"";position:absolute;left:0;width:90px;height:2px;top:-1px;background:var(--accent)}
.contact .row{position:absolute;left:122px;display:flex;gap:14px;font-size:19px;line-height:23px}
.contact .btn{position:absolute;left:125px;top:277px;height:35px;padding:0 14px;font-size:17px}

.footer{position:absolute;left:0;top:2711px;width:1200px;height:364px;background:var(--footer-bg);color:var(--footer-text)}
.footer h4{font-size:13px;font-weight:600;color:var(--white)}
.newsletter{position:absolute;left:183px;top:67px;width:249px}
.newsletter p{font-size:11.5px;margin:18px 0 24px}
.newsletter .field{height:37px;background:var(--white);color:#555;font-size:11px;padding:12px 10px}
.newsletter .sub{margin-top:8px;height:37px;background:var(--accent);color:var(--white);font-size:11px;text-align:center;line-height:37px}
.overview{position:absolute;left:585px;top:67px}
.overview ul{list-style:none;margin-top:18px;font-size:11.5px;line-height:23px}
.foot-brand{position:absolute;left:800px;top:50px;width:220px;text-align:center}
.foot-brand strong{display:block;font-size:34px;font-weight:300;color:var(--white);line-height:40px}
.foot-brand small{font-size:17px;font-weight:300;color:var(--white)}
.foot-brand .loc{display:block;font-size:11.5px;margin-top:8px}
.foot-brand .join{display:block;font-size:17px;margin-top:48px}
.socials{display:flex;justify-content:center;gap:22px;margin-top:14px}
.socials i{width:21px;height:21px;border:2px solid var(--footer-text);border-radius:3px}
.copy-rule{position:absolute;left:172px;top:277px;width:856px;height:1px;background:#444}
.copyright{position:absolute;top:308px;width:100%;text-align:center;font-size:16.5px}
</style>
</head>
<body>

<div class="hero" role="img" aria-label="Evening photo of the arcade storefronts lit under a blue twilight sky"></div>
<div class="brand"><small>The Arcade at</small><strong>Fernbrook</strong></div>
<nav class="main-nav">
  <a href="#" class="active">HOME</a><a href="#">TRENDING</a><a href="#">DIRECTORY</a><a href="#">HAPPENING</a><a href="#">BLOG</a><a href="#">VISIT</a>
  <svg class="search" width="14" height="14" viewBox="0 0 14 14"><circle cx="8" cy="6" r="4" fill="none" stroke="#555" stroke-width="1.2"/><path d="M5 9 1.5 12.5" stroke="#555" stroke-width="1.2"/></svg>
</nav>

<section class="intro">
  <h1>Suitable Stores &amp; Offices for<br><em>IT Tech Businesses</em></h1>
  <a class="btn" href="#">Inquiry Now <span>›</span></a>
  <p class="note">Limited Units <i></i> Limited Time</p>
</section>
<div class="hours">
  <svg width="66" height="66" viewBox="0 0 66 66"><circle cx="30" cy="33" r="30" fill="none" stroke="rgba(255,255,255,.35)" stroke-width="3"/><path d="M30 14v19l10 10" fill="none" stroke="rgba(255,255,255,.35)" stroke-width="3"/></svg>
  <p>VISITING HOURS:<b>10 AM - 7 PM</b></p>
</div>

<section class="why">
  <h2 class="sec-title">Why Fernbrook<span>shopping center?</span></h2>
  <div class="rule"></div>
  <div class="features">
    <div class="feature">
      <svg width="64" height="64" viewBox="0 0 64 64" fill="none" stroke="#6f86c6" stroke-width="2"><circle cx="32" cy="32" r="28"/><circle cx="32" cy="32" r="17"/><circle cx="32" cy="32" r="7"/><path d="M32 0v20M32 44v20M0 32h20M44 32h20"/></svg>
      <h3>Niche Market</h3>
      <p>Lorem ipsum dolor sit amet, consecte-tur adipiscing elit, sed do eiusmod tempor incididunt ut labore et dolore magna aliqua. Quis ipsum suspendisse ultrices gravida.</p>
    </div>
    <div class="feature">
      <svg width="64" height="64" viewBox="0 0 64 64" fill="none" stroke="#6f86c6" stroke-width="2"><path d="M4 58 12 34h10M42 34h10l8 24zM4 58h56"/><path d="M32 44C22 32 20 26 20 20a12 12 0 0 1 24 0c0 6-2 12-12 24z"/><circle cx="32" cy="20" r="5"/></svg>
      <h3>Accessibility</h3>
      <p>Lorem ipsum dolor sit amet, consecte-tur adipiscing elit, sed do eiusmod tempor incididunt ut labore et dolore magna aliqua. Quis ipsum suspendisse ultrices gravida.</p>
    </div>
    <div class="feature">
      <svg width="64" height="64" viewBox="0 0 64 64" fill="none" stroke="#6f86c6" stroke-width="2"><path d="M4 44h10l10 4h14a3 3 0 0 1 0 6H24M38 54l16-8a3 3 0 0 1 4 4L40 62H4"/><path d="M40 40V22M40 28c-8 0-12-4-12-10 8 0 12 4 12 10zM40 24c0-8 4-12 12-12 0 8-4 12-12 12z"/></svg>
      <h3>Investment</h3>
      <p>Lorem ipsum dolor sit amet, consecte-tur adipiscing elit, sed do eiusmod tempor incididunt ut labore et dolore magna aliqua. Quis ipsum suspendisse ultrices gravida.</p>
    </div>
  </div>
</section>

<div class="band" role="img" aria-label="Daytime photo of the arcade buildings with bare trees and parked cars"></div>
<section class="partners">
  <h2 class="sec-title">Don't miss the opportunity<span>Be with the bests</span></h2>
  <div class="rule"></div>
  <div class="tenants">
    <span>Telvora</span><span>Quillsoft</span><span>Voltane</span><span>Sonique</span>
    <span>Northwire</span><span>Stridewell</span><span>Tickmark</span><span>Verbena</span>
  </div>
  <a class="btn" href="#">View Directory <span>›</span></a>
</section>

<h2 class="sec-title gallery-title">Gallery</h2>
<div class="rule gallery-rule"></div>
<div class="shot" style="left:184px;top:1803px;width:191px;height:191px;background:linear-gradient(180deg,#eceae4,#b79c77 55%,#2b2a26)" role="img" aria-label="Interior atrium with a stone wall and railing"></div>
<div class="shot" style="left:398px;top:1803px;width:191px;height:191px;background:linear-gradient(180deg,#3d73c9,#9ec0e8 40%,#ecebe6 60%,#8b8172)" role="img" aria-label="White tower building under a blue sky"></div>
<div class="shot" style="left:611px;top:1803px;width:405px;height:402px;background:linear-gradient(120deg,#ebe6da 0%,#d8cbb4 35%,#3a72cc 60%,#8f8f8f 85%,#c9463c)" role="img" aria-label="Curving walkway along storefronts on a sunny day"></div>
<div class="shot" style="left:184px;top:2015px;width:191px;height:190px;background:linear-gradient(180deg,#3f74cc,#a9c4e6 40%,#e6e2d8 62%,#6b5a4a)" role="img" aria-label="Corner storefront with parked cars"></div>
<div class="shot" style="left:398px;top:2015px;width:191px;height:190px;background:linear-gradient(180deg,#2e3340,#3b3e46 60%,#262626)" role="img" aria-label="More gallery photos of the center at dusk">
  <svg width="46" height="46" viewBox="0 0 46 46" style="position:absolute;left:72px;top:72px"><circle cx="23" cy="23" r="21" fill="none" stroke="#fff" stroke-width="1.5"/><path d="M23 13v20M13 23h20" stroke="#fff" stroke-width="1.5"/></svg>
</div>

<div class="map" role="img" aria-label="Dark street map of the area around the arcade with nearby places marked"></div>
<section class="contact">
  <h2>Contact</h2>
  <div class="line"></div>
  <div class="row" style="top:150px">
    <svg width="26" height="32" viewBox="0 0 26 32" fill="none" stroke="#6f86c6" stroke-width="2"><path d="M13 30C4 19 2 15 2 11a11 11 0 0 1 22 0c0 4-2 8-11 19z"/><circle cx="13" cy="11" r="4"/></svg>
    <span>2870 Briarwell Pkwy<br>Larkfield GA 30917</span>
  </div>
  <div class="row" style="top:212px">
    <svg width="26" height="26" viewBox="0 0 26 26" fill="none" stroke="#6f86c6" stroke-width="2"><path d="M6 2l5 5-3 4c2 4 4 6 8 8l4-3 5 5-4 4C11 25 1 15 2 6z"/></svg>
    <span>404 555 0172</span>
  </div>
  <a class="btn" href="#">Directions <span>›</span></a>
</section>

<footer class="footer">
  <div class="newsletter">
    <h4>JOIN OUR NEWSLETTER</h4>
    <p>Join our email list for the latest news</p>
    <div class="field">your@email.com</div>
    <div class="sub">Subscribe</div>
  </div>
  <div class="overview">
    <h4>OVERVIEW</h4>
    <ul><li>Stores</li><li>Advertising</li><li>Offices</li><li>Customer Service</li><li>Blog</li></ul>
  </div>
  <div class="foot-brand">
    <small>The Arcade at</small>
    <strong>Fernbrook</strong>
    <span class="loc">Located in Larkfield USA</span>
    <span class="join">Join Our Social Networks</span>
    <div class="socials"><i></i><i></i><i></i></div>
  </div>
  <div class="copy-rule"></div>
  <p class="copyright">© Copyright 2020 The Arcade at Fernbrook. All Rights Reserved</p>
</footer>

</body>
</html>
```